Redesign of the Molvekraut label

I am a pharmacist and sell a bitters called "Molvekraut". I would like to revise and modernize the current logo of my "Molvekraut". I have attached a photo of the current label. I have different bottle sizes with different label sizes, but for now I will only need one label for the 700ml size:
20ml 36x47mm
40ml 45x62mm
200ml 70x91mm
350ml 70x98mm
500ml 70x110mm
700ml 87x119mm
The Molve is a small stream that runs through our town. The Molvekraut is a play on words that takes up the mysticism of the Harz, as a spirit can of course also be a schnapps. I like the mysticism and rough nature of the Harz in connection with the product. I have attached a logo suggestion that I once had an AI design. But I am very open to new ideas. A connection to my pharmacy does not necessarily have to be recognizable. VG, K. Harmsen

Target Market(s)

End consumers, gastronomy, restaurants, hotels

```html
<!DOCTYPE html>
<html lang="de">
<head>
<meta charset="utf-8">
<title>Molvekraut – Etikett 700 ml</title>
<link href="https://fonts.googleapis.com/css2?family=Abril+Fatface&family=Libre+Baskerville:ital,wght@0,400;0,700;1,400&display=swap" rel="stylesheet">
<style>
  :root {
    --page: #ffffff;
    --paper: #efebe3;
    --paper-shade: #e4dfd4;
    --ink: #121009;
    --ink-brown: #3a2d17;
    --ochre: #a2733c;
    --umber: #6e5127;
    --forest: #3a2d17;
    --cream: #ffffff;
    --dots: rgba(255,255,255,0.45);
  }
  * { margin: 0; padding: 0; box-sizing: border-box; }
  html, body { width: 1200px; height: 927px; overflow: hidden; background: var(--page); }
  .canvas { position: relative; width: 1200px; height: 927px; }

  .label {
    position: absolute; left: 331px; top: 112px; width: 539px; height: 704px;
    border-radius: 10px; overflow: hidden;
    background: linear-gradient(180deg, var(--paper) 0%, var(--paper-shade) 50%, var(--paper) 100%);
    box-shadow: 0 2px 8px rgba(0,0,0,0.35);
    font-family: "Libre Baskerville", Georgia, serif;
  }
  .label svg { position: absolute; left: 0; top: 0; overflow: visible; }

  .landscape {
    position: absolute; left: 0; top: 254px; width: 539px; height: 200px;
    background: linear-gradient(180deg, var(--ochre) 0%, var(--umber) 45%, var(--forest) 100%);
  }
  .lower-field {
    position: absolute; left: 0; top: 454px; width: 539px; height: 250px;
    background: var(--forest);
  }

  .product-type {
    position: absolute; left: 0; width: 539px; top: 308px;
    text-align: center; color: var(--cream);
    font-weight: 700; font-size: 24px; letter-spacing: 0.5px;
  }
  .product-type-rule {
    position: absolute; left: 180px; top: 339px; width: 193px; height: 1px;
    background: rgba(255,255,255,0.5);
  }

  .story {
    position: absolute; left: 0; width: 556px; top: 433px;
    text-align: center; color: var(--cream);
    font-style: italic; font-size: 13.4px; line-height: 16.4px; letter-spacing: 0.9px;
  }

  .maker-frame {
    position: absolute; left: 63px; top: 532px; width: 413px; height: 124px;
    border-top: 1.5px dotted var(--dots); border-bottom: 1.5px dotted var(--dots);
  }
  .maker-divider {
    position: absolute; left: 317px; top: 545px; height: 100px;
    border-left: 1.5px dotted var(--dots);
  }
  .maker {
    position: absolute; left: 67px; top: 535px; color: var(--cream);
  }
  .maker .from { font-style: italic; font-size: 11.5px; line-height: 14px; padding-left: 2px; }
  .maker .pharmacy { font-weight: 700; font-size: 17.5px; line-height: 20px; letter-spacing: 0.2px; }
  .maker .town { font-size: 20px; line-height: 22px; }
  .maker .pharmacist { font-style: italic; font-size: 14px; line-height: 17px; margin-top: 3px; padding-left: 2px; }
  .maker .address { font-style: italic; font-size: 11.5px; line-height: 14.2px; padding-left: 2px; }

  .herb-art {
    position: absolute; left: 329px; top: 545px; width: 136px; height: 48px;
    background: radial-gradient(ellipse at 50% 50%, #d9d4c8 0%, #9a917e 60%, rgba(58,45,23,0) 100%);
    border-radius: 50% 40% 50% 40%;
  }
  .herb-rule {
    position: absolute; left: 329px; top: 600px; width: 147px;
    border-top: 1.5px dotted var(--dots);
  }
  .volume {
    position: absolute; left: 322px; width: 150px; top: 604px;
    text-align: center; color: var(--cream);
  }
  .volume .size { font-style: italic; font-size: 36px; line-height: 38px; letter-spacing: -0.5px; }
  .volume .abv { font-weight: 700; font-size: 12px; line-height: 12px; margin-top: -3px; }
</style>
</head>
<body>
<div class="canvas">
  <div class="label">
    <div class="landscape" role="img" aria-label="Landschaft mit Harzbergen, Vögeln und dunklem Nadelwald"></div>
    <div class="lower-field"></div>

    <svg class="label-headings" width="539" height="704" viewBox="0 0 539 704">
      <defs>
        <path id="origin-arc" d="M139,121 Q281,81 425,121"/>
        <path id="craft-arc" d="M109,358 Q276,393 447,350"/>
      </defs>
      <rect x="117" y="110" width="7" height="7" fill="var(--ink-brown)" transform="rotate(20 120 113)"/>
      <rect x="432" y="109" width="7" height="7" fill="var(--ink-brown)" transform="rotate(-15 435 112)"/>
      <text font-family="Libre Baskerville, Georgia, serif" font-weight="700" font-size="31" fill="var(--ink-brown)" letter-spacing="1">
        <textPath href="#origin-arc" startOffset="50%" text-anchor="middle">MOLVETALER</textPath>
      </text>
      <text x="278" y="125" text-anchor="middle" font-family="Libre Baskerville, Georgia, serif" font-weight="700" font-size="16" fill="var(--ink-brown)">ERLESENER</text>
      <text x="37" y="233" textLength="479" lengthAdjust="spacingAndGlyphs" font-family="Abril Fatface, Georgia, serif" font-size="95" fill="var(--ink)">MOLVEKRAUT</text>

      <circle cx="102" cy="344" r="2.2" fill="var(--cream)"/>
      <circle cx="453" cy="344" r="2.2" fill="var(--cream)"/>
      <text font-family="Libre Baskerville, Georgia, serif" font-style="italic" font-size="18.5" fill="var(--cream)">
        <textPath href="#craft-arc" startOffset="50%" text-anchor="middle">NACH ALTER APOTHEKERKUNST</textPath>
      </text>
    </svg>

    <div class="product-type">BITTERLIKOR</div>
    <div class="product-type-rule"></div>

    <p class="story">Eine Zubereitung nach höchst geheimem Rezept. Sie sei<br>empfohlen zum Genuss nach einem guten Mahl.<br>Aufs Feinste zubereitet mit geistigen Auszügen von Enzian,<br>Kalmus, Malabar-Kardamom und anderen wertvollen Zutaten.</p>

    <div class="maker-frame"></div>
    <div class="maker-divider"></div>
    <div class="maker">
      <div class="from">Aus der</div>
      <div class="pharmacy">LINDEN APOTHEKE</div>
      <div class="town">Molvetal</div>
      <div class="pharmacist">Dr. Kai Harmsen</div>
      <div class="address">Brunnenweg 12<br>38999 Molvetal<br>Tel. 05500-1234</div>
    </div>

    <div class="herb-art" role="img" aria-label="Gravierte Zeichnung eines Kräuterblattes"></div>
    <div class="herb-rule"></div>
    <div class="volume">
      <div class="size">700ML</div>
      <div class="abv">34% VOL</div>
    </div>
  </div>
</div>
</body>
</html>
```